Window Company website re-design

We are creating a new website design for http://harborpanes.example and we are going to be using wordpress for the site. The idea is to make it appeal to homeowners, more than half of the visitors will be female so the design must appeal to them with appropriate colors and shapes. Historically the website has been dark with a black background and the idea is to keep some of that but make it much brighter with textures and inviting colors.
Major competitors which we will mimic are the following in order of favorites:
http://www.birchvalleyglass.example/ (this is something we really like because of the full width, call to action, easy to navigate, space for
http://www.grainhillexteriors.example/ (this is a nice wide design with a lot of great image space and call to actions)
http://www.restorebyhollister.example/ (the full width is nice here)
http://www.duskpointpanes.example/ (the slide over option showing the window is nice here.)
Others:
http://www.torvane.example/
http://www.quiro.example/home/default.aspx
http://www.hollisterpanes.example/
https://www.glazeplanet.example/
http://www.delcot.example/

Harbor is the leader in the industry so they want a design that is going to portray that. The owners say that their competitors always copy what they do so this design must be cutting edge.

Important elements need to included:
1. Make the design convey very obviously they are a replacement window and door company.
2. Very clear “request a free estimate” call to action box on the homepage.
3. Area for the “Live Support” call to action
4. Navigation:

- Home
- Why Harbor
o Saves Dollars, Makes Sense
o We Have You Covered Start to Finish
o The Harbor Difference
o Pitfalls to Avoid
- Windows and Doors
o Windows
 Double Hung Windows
 Awning Windows
 Basement Hopper Windows
 Bow Windows
 Garden Windows
 Casement Windows
 Bay Windows
 Slider Windows
 Dead-Lite / Specialty / Transom
o Doors
 Storm Doors
 Harbor French Doors
 Patio Slider Doors
 Door Catalog
 Keypad Deadbolt
o Before and After
- About Us
o Testimonials
o Directions
o Warranty
o Employment
o Manufacturing process
o Home Shows
o Community Involvement
- Financing
- Commercial Division
- Careers
- Contact Us

Important elements for the Home Page:
1. Call to action – request a free quote
2. Awards
3. Live support
4. Guarantee
5. Featured testimonials
6. Press releases
7. Locations (Map?)

The attached photos can be used for the homepage images

Target Market(s)

The target market is middle income home owners who want good quality and great service.

Industry/Entity Type

Industry

Font styles to use
Sans Serif

Colors

Designer to choose colors to be used in the design.

Requirements
Must have
• We will need 2 designs, one for the homepage and the other for the inner pages.

2. Awards
3. Live support
4. Guarantee
5. Featured testimonials
6. Press releases
7. Locations (Map?)

```html
<!DOCTYPE html>
<html lang="en">
<head>
<meta charset="utf-8">
<title>Harbor Windows</title>
<link href="https://fonts.googleapis.com/css2?family=Bitter:wght@400;500;700&family=Noto+Sans:ital,wght@0,400;0,700;1,400&display=swap" rel="stylesheet">
<style>
:root{
  --ink:#3b4a63;
  --ink-soft:#5a6678;
  --green:#84b100;
  --green-dark:#6f9700;
  --panel:#e5eaee;
  --rule:#c9d1da;
  --orange:#f58a00;
  --orange-light:#ffa726;
  --navy:#1d2a3d;
  --hero-a:#2c3a2a;
  --hero-b:#5c6b58;
  --white:#ffffff;
}
*{box-sizing:border-box;margin:0;padding:0}
html,body{width:1200px;height:1000px;overflow:hidden}
body{background:var(--white);font-family:"Noto Sans",sans-serif;color:var(--ink);position:relative;font-size:15px;line-height:24px}
a{text-decoration:none}
.copy{letter-spacing:-0.35px}
.link{font-family:"Bitter",serif;font-weight:700;color:var(--green);font-size:15px}

.hero{position:absolute;left:0;top:0;width:1200px;height:100px;background:linear-gradient(90deg,var(--hero-a),var(--hero-b) 45%,#3d4a3a 75%,#6b7669)}
.hero-dashes{position:absolute;left:0;top:95px;width:1200px;height:5px;background:repeating-linear-gradient(90deg,var(--white) 0 10px,transparent 10px 16px)}
.hero-copy{position:absolute;left:118px;top:-14px;width:620px;font-family:"Bitter",serif;font-size:20px;line-height:30px;color:var(--white);letter-spacing:-0.2px}
.quote-btn{position:absolute;left:780px;top:-20px;width:300px;height:64px;background:linear-gradient(#8b95a2,#68727f);border-radius:0 0 4px 4px;overflow:hidden}
.quote-btn .label{position:absolute;left:18px;top:27px;font-family:"Bitter",serif;font-weight:700;font-size:16px;color:var(--white)}
.quote-btn svg{position:absolute;right:0;top:0}

.about{position:absolute;left:121px;top:142px;width:625px}
.about p{font-size:15px;line-height:24px;color:var(--ink-soft)}
.about .link{display:block;margin-top:9px}

.guarantee{position:absolute;left:780px;top:145px;width:300px;height:189px;background:var(--panel);border-radius:3px}
.ribbon{position:absolute;left:773px;top:146px}
.ribbon-text{position:absolute;left:797px;top:152px;font-family:"Bitter",serif;font-weight:500;font-size:24px;color:var(--white);transform:rotate(-2deg);transform-origin:left}
.guarantee-body{position:absolute;left:800px;top:200px;width:265px;font-size:15px;line-height:24px;color:var(--ink-soft)}
.guarantee-body strong{color:var(--ink)}
.guarantee-body .link{display:block;margin-top:1px}

.rule{position:absolute;left:120px;width:960px;height:1px;background:var(--rule)}

h2{font-family:"Bitter",serif;font-weight:500;font-size:22px;line-height:30px;color:var(--ink);position:absolute}
.testimonial{position:absolute;left:120px;top:461px;width:630px;height:110px;background:var(--panel);border-radius:3px;padding:16px 20px;font-style:italic;color:var(--ink-soft);font-size:15px;line-height:24px}
.testimonial::before{content:"";position:absolute;left:30px;top:-10px;border:10px solid transparent;border-top:0;border-bottom-color:var(--panel)}
.press{position:absolute;left:780px;top:454px;width:302px;font-size:15px;line-height:24px;color:var(--ink-soft)}
.press strong{color:var(--ink)}

.awards{position:absolute;left:120px;top:665px;width:962px;height:70px}
.sep{position:absolute;top:15px;width:1px;height:40px;background:var(--rule)}
.badge{position:absolute;background:#c9ccd0;border-radius:3px}
.awards .note{position:absolute;left:760px;top:16px;font-size:13px;line-height:21px;color:var(--ink-soft);width:210px;letter-spacing:-0.3px}

.contact-band{position:absolute;left:0;top:750px;width:1200px;height:100px;background:var(--panel)}
.address{position:absolute;left:119px;top:775px;font-size:15px;line-height:24px;color:var(--ink-soft)}
.address strong{color:var(--ink)}
.address .email{color:var(--green);font-weight:700}
.vsep{position:absolute;left:529px;top:775px;width:1px;height:50px;background:var(--rule)}
.thumb{position:absolute;left:558px;top:775px;width:50px;height:50px;background:linear-gradient(#8a96a0,#3d4650)}
.directions{position:absolute;left:626px;top:775px;font-size:15px;line-height:24px;font-weight:700}
.directions .t{color:var(--ink)}
.directions a{color:var(--green)}
.social{position:absolute;left:970px;top:792px;display:flex;gap:10px}
.social span{display:block;width:20px;height:20px;background:#9aa3ae}

.nav{position:absolute;left:0;top:850px;width:1200px;height:50px;background:var(--green)}
.nav ul{list-style:none;position:absolute;left:120px;width:960px;top:13px;display:flex;justify-content:space-between}
.nav a{color:var(--white);font-weight:700;font-size:14px;letter-spacing:-0.2px}
.legal{position:absolute;left:0;top:900px;width:1200px;height:100px;background:var(--navy)}
.legal p{position:absolute;left:118px;top:12px;font-size:13px;color:#a9b2bf;letter-spacing:-0.3px}
</style>
</head>
<body>

<header class="hero" role="img" aria-label="Photo of a home with new replacement windows">
  <p class="hero-copy">with high-performance Harbor Windows is one of the wisest home improvement investments you’ll ever make.</p>
  <a class="quote-btn" href="#">
    <span class="label">Click to request a quotation</span>
    <svg width="64" height="64" viewBox="0 0 64 64"><polygon points="20,0 64,0 64,64 6,64" fill="#84b100"/><polyline points="36,20 44,32 36,44" fill="none" stroke="#3b4a20" stroke-width="5"/></svg>
  </a>
</header>
<div class="hero-dashes"></div>

<section class="about copy">
  <p>For over 30 years we have been designing windows to fit your world. We offer a wide selection of top quality, custom-made windows to fit your home because we know you appreciate variety, expect quality and demand affordability. Our windows are a reflection of our dedication and commitment to excellence. The skill and care our people take in manufacturing quality replacement windows originates from the tremendous pride we exhibit in all phases of production, including precise engineering and thorough quality control testing. All windows are made in the USA.</p>
  <a class="link" href="#">Find out more about us ›</a>
</section>

<aside class="guarantee"></aside>
<svg class="ribbon" width="314" height="54" viewBox="0 0 314 54">
  <polygon points="0,12 313,0 313,40 6,50" fill="#e07a00"/>
  <polygon points="0,10 313,0 313,38 3,46" fill="#f58a00"/>
  <polygon points="0,10 313,0 313,12 0,22" fill="#ffa726" opacity=".6"/>
</svg>
<div class="ribbon-text">Our Guarantee …</div>
<div class="guarantee-body copy">
  <p>We are so confident in our work that we offer one of the best guarantees in the industry.</p>
  <p><strong>We cover everything 100%.</strong></p>
  <a class="link" href="#">Find out more ›</a>
</div>

<div class="rule" style="top:380px"></div>

<h2 style="left:120px;top:415px">What do our customers think?</h2>
<blockquote class="testimonial copy">“Lorem ipsum dolor sit amet, consectetur adipisicing sed do eiusmod tempor incididunt ut labore et dolore magna aliqua. Ut enim ad minim veniam, quis nostrud exercitation ullamco laboris nisi ut aliquip ex ea commodo consequat duis aute in reprehenderit.”</blockquote>
<a class="link" href="#" style="position:absolute;left:121px;top:580px">Read more testimonials ›</a>

<h2 style="left:778px;top:415px">Latest Press Release</h2>
<div class="press copy">
  <p><strong>Press Release Title in here.</strong></p>
  <p>Lorem ipsum dolor sit adipisicing elit sed do eiusmod tempor incididunt ut labore dolore magna aliqua enim ad minim veniam, quis nostrud exercitation ullamco laboris …</p>
</div>
<a class="link" href="#" style="position:absolute;left:780px;top:580px">Read more ›</a>

<div class="rule" style="top:650px"></div>

<div class="awards">
  <div class="badge" style="left:0;top:1px;width:68px;height:68px;border-radius:50%"></div>
  <div class="sep" style="left:108px"></div>
  <div class="badge" style="left:145px;top:24px;width:150px;height:26px"></div>
  <div class="sep" style="left:332px"></div>
  <div class="badge" style="left:366px;top:20px;width:136px;height:32px"></div>
  <div class="sep" style="left:541px"></div>
  <div class="badge" style="left:588px;top:20px;width:154px;height:32px"></div>
  <p class="note">Ranked in the Trusted Renovator Top 10 for the last 7 years</p>
</div>

<footer>
  <div class="contact-band"></div>
  <p class="address copy"><strong>Harbor Windows .</strong> 42 Linden Ct . Westbrook . NJ 08099<br>Phone: (800) 555 - 0147 &nbsp; | &nbsp; <a class="email" href="#">Click here to email us</a></p>
  <div class="vsep"></div>
  <div class="thumb" role="img" aria-label="Photo of the Harbor Windows showroom building"></div>
  <p class="directions copy"><span class="t">How to find us</span><br><a href="#">Click here for directions</a></p>
  <div class="social">
    <span aria-label="Social profile"></span>
    <span aria-label="Social profile"></span>
    <svg width="20" height="20" viewBox="0 0 20 20" aria-label="Email"><rect width="20" height="20" fill="#9aa3ae"/><rect x="3" y="5" width="14" height="10" fill="#fff"/><polyline points="3,5 10,11 17,5" fill="none" stroke="#9aa3ae" stroke-width="1.5"/></svg>
    <span aria-label="Social profile"></span>
  </div>

  <nav class="nav">
    <ul>
      <li><a href="#">Home</a></li>
      <li><a href="#">Why Harbor?</a></li>
      <li><a href="#">Windows &amp; Doors</a></li>
      <li><a href="#">About Us</a></li>
      <li><a href="#">Financing</a></li>
      <li><a href="#">Commercial Division</a></li>
      <li><a href="#">Careers</a></li>
      <li><a href="#">Contact Us</a></li>
    </ul>
  </nav>
  <div class="legal"><p>© Copyright 2014 Harbor Windows</p></div>
</footer>

</body>
</html>
```